Velimo Ventures Logo and Business Card Design

We already have the rough logo shape (however please make the lines on the logo much thicker so a dark background is not required to see it) . see photos uploaded.
It needs to be refined with color and digitized and then have a front and back business card layout done.
The services are high vibration healing support through a therapy and feng shui service offering. We want people to Feel Happiness, Feel Prosperity and Feel Peace. (the back of the card would have these phrases on it) So a warm, calm and peaceful feeling card.
We would like the card to use the logo provided (with thicker lines and color added) but below the graphic please use the name "Velimo Ventures" NOT Velimo.
We also would like to use the colors in the colorized matrix shown in photos (gold and purple) but on the lighter side. Thanks for your time!

Front of Card should include: Logo, with Company Name: Velimo Ventures as part of logo, Name: Mara Donne email: mara@velimo.example web: www.velimo.example mobile: 555.018.2946 at bottom of front list Family Constellation | Feng Shui

Back of Card should have the logo and the following listed vertically:

PERSONAL | BUSINESS (Larger size then smaller bullet items below)
*Find Happiness
*Find Prosperity
*Find Peace

Target Market(s)

Target market is both business and personal

Contact Information for Business Card

Front of Card should include: Logo, with Company Name: Velimo Ventures as part of logo, Name: Mara Donne email: mara@velimo.example web: www.velimo.example mobile: 555.018.2946 at bottom of front list Family Constellation | Feng Shui ++++ Back of Card should have the logo and the following listed vertically: PERSONAL | BUSINESS (Larger size then smaller bullet items below) *Find Happiness *Find Prosperity *Find Peace

Font styles to use
Sans Serif

Colors

Designer to choose colors to be used in the design.

Requirements
Nice to have
• Nice light contrast color for the back of card background
Should not have
• No dark colored background on Card.

```html
<!DOCTYPE html>
<html lang="en">
<head>
<meta charset="utf-8">
<title>Velimo Ventures – Business Card</title>
<link rel="stylesheet" href="https://fonts.googleapis.com/css2?family=Marcellus&family=Montserrat:wght@400;600&family=Lora:wght@400;500&display=swap">
<style>
  :root {
    --canvas: #ababab;
    --card: #ffffff;
    --purple: #944796;
    --purple-deep: #93469a;
    --orchid: #dc8ddf;
    --gold: #c9a24e;
    --gold-light: #ecd08a;
    --text-grey: #7a7a7a;
    --rule: #c8c8c8;
    --white: #ffffff;
  }
  * { margin: 0; padding: 0; box-sizing: border-box; }
  html, body { width: 1200px; height: 1000px; overflow: hidden; }
  body { background: var(--canvas); position: relative; }

  .card {
    position: absolute;
    left: 294px;
    width: 613px;
    height: 352px;
    border-radius: 24px;
    overflow: hidden;
  }
  .card--front { top: 95px; background: var(--card); }
  .card--back {
    top: 535px;
    background:
      linear-gradient(128deg, #b35fb6 0%, var(--orchid) 30%, #c87ccd 45%, var(--purple-deep) 66%, var(--purple-deep) 100%);
  }

  .brand {
    position: absolute;
    display: flex;
    align-items: center;
    gap: 12px;
    font-family: "Marcellus", serif;
    font-weight: 400;
    white-space: nowrap;
  }
  .brand__dot { border-radius: 50%; flex: none; }
  .brand--front {
    top: 50px; left: 0; right: 0; justify-content: center;
    color: var(--purple); font-size: 34px; letter-spacing: 1px;
  }
  .brand--front .brand__dot { width: 34px; height: 34px; border: 4px solid var(--gold); }
  .brand--back {
    left: 30px; top: 270px; color: var(--white); font-size: 26px; letter-spacing: 1px;
  }
  .brand--back .brand__dot { width: 30px; height: 30px; border: 2px solid var(--white); }

  .holder-name {
    position: absolute; right: 330px; top: 176px;
    text-align: right; white-space: nowrap;
    font-family: "Marcellus", serif; font-weight: 400;
    font-size: 31px; line-height: 36px; color: var(--purple);
  }

  .contact-list {
    position: absolute; left: 322px; top: 166px;
    list-style: none;
    font-family: "Montserrat", sans-serif; font-size: 17px; color: var(--text-grey);
  }
  .contact-list li { display: flex; align-items: center; gap: 10px; height: 23px; white-space: nowrap; }
  .contact-list svg { width: 12px; height: 12px; fill: var(--purple); flex: none; }
  .contact-list .contact--phone { font-weight: 600; }

  .divider {
    position: absolute; left: 51px; right: 51px; top: 295px;
    border-top: 1px solid var(--rule);
  }
  .services {
    position: absolute; left: 0; right: 0; top: 309px; text-align: center;
    font-family: "Marcellus", serif; font-size: 17.5px; letter-spacing: 1.6px;
    color: var(--purple);
  }

  .audience {
    position: absolute; left: 42px; top: 104px;
    font-family: "Marcellus", serif; font-size: 20px; letter-spacing: 3.3px;
    color: var(--gold-light);
  }
  .promises {
    position: absolute; left: 44px; top: 139px; list-style: none;
    font-family: "Lora", serif; font-weight: 500;
    font-size: 22.5px; line-height: 29px; color: var(--white);
  }
</style>
</head>
<body>

<section class="card card--front">
  <div class="brand brand--front"><span class="brand__dot"></span>VELIMO VENTURES</div>

  <h1 class="holder-name">Mara Donne</h1>

  <ul class="contact-list">
    <li class="contact--phone">
      <svg viewBox="0 0 12 12"><path d="M3 0h6a1 1 0 0 1 1 1v10a1 1 0 0 1-1 1H3a1 1 0 0 1-1-1V1a1 1 0 0 1 1-1zm.6 1.4v8.4h4.8V1.4z"/></svg>
      555.018.2946
    </li>
    <li>
      <svg viewBox="0 0 12 12"><path d="M0 2h12v8H0zM1 3v.4l5 3.2 5-3.2V3zm0 1.6V9h10V4.6L6 7.8z"/></svg>
      mara@velimo.example
    </li>
    <li>
      <svg viewBox="0 0 12 12"><path d="M6 0a6 6 0 1 0 0 12A6 6 0 0 0 6 0zm-.5 1.1v2.4H3.7c.4-1.3 1-2.2 1.8-2.4zm1 0c.8.2 1.4 1.1 1.8 2.4H6.5zM3.5 4.5h2v2.5h-2.1a9 9 0 0 1 .1-2.5zm3 0h2a9 9 0 0 1 .1 2.5H6.5zM1.1 5h1.4a10 10 0 0 0 0 2H1.1a5 5 0 0 1 0-2zm8.4 0h1.4a5 5 0 0 1 0 2H9.5a10 10 0 0 0 0-2zM3.6 8h1.9v2.9C4.7 10.6 4 9.5 3.6 8zm2.9 0h1.9c-.4 1.5-1.1 2.6-1.9 2.9z"/></svg>
      www.velimo.example
    </li>
  </ul>

  <div class="divider"></div>
  <p class="services">FAMILY CONSTELLATION | FENG SHUI</p>
</section>

<section class="card card--back">
  <p class="audience">PERSONAL | BUSINESS</p>
  <ul class="promises">
    <li>*Find Happiness</li>
    <li>*Find Prosperity</li>
    <li>*Find Peace</li>
  </ul>
  <div class="brand brand--back"><span class="brand__dot"></span>VELIMO VENTURES</div>
</section>

</body>
</html>
```